Business Card Design Project

use presentation folder design and my logo and make 4 over 4 business cards

Industry/Entity Type

Business

Requirements
Must have
• use the design from my presentation folder and put my logo on it

Name
Title
phone
fax
email

```html
<!DOCTYPE html>
<html lang="en">
<head>
<meta charset="utf-8">
<title>Brightwell Counseling – Business Cards</title>
<link href="https://fonts.googleapis.com/css2?family=Lora:wght@400;700&family=Quicksand:wght@400;500&display=swap" rel="stylesheet">
<style>
  :root{
    --stage:#6f6f6f;
    --card-front:#efe6dd;
    --card-back-edge:#cfb49a;
    --card-back-mid:#e9d9c9;
    --blob:#f3ebe3;
    --blob-soft:#e6d7c8;
    --brown:#8a5420;
    --brown-dark:#6b3f15;
    --ink:#2b2118;
    --grey:#7d7d7d;
  }
  *{box-sizing:border-box;margin:0;padding:0}
  html,body{width:1200px;height:900px;overflow:hidden}
  body{background:var(--stage);position:relative;font-family:"Lora",serif}
  .card{position:absolute;width:560px;height:320px;overflow:hidden;box-shadow:0 14px 30px rgba(0,0,0,.35)}
  .card-front{left:90px;top:90px;background:var(--card-front)}
  .card-back{left:560px;top:470px;background:radial-gradient(ellipse at 50% 45%,var(--card-back-mid) 30%,var(--card-back-edge) 100%)}
  .card svg.decor{position:absolute;inset:0;width:100%;height:100%}
  .brand{position:absolute;display:flex;align-items:center;gap:10px}
  .brand-dot{width:18px;height:18px;border-radius:50%;background:var(--brown)}
  .brand-name{font-family:"Lora",serif;font-weight:400;color:var(--brown);line-height:1}
  .brand-tagline{font-family:"Quicksand",sans-serif;color:var(--ink);letter-spacing:.5px}
  .card-front .brand{left:36px;top:112px}
  .card-front .brand-name{font-size:30px}
  .card-front .brand-tagline{position:absolute;left:64px;top:156px;font-size:12px}
  .person{position:absolute;right:40px;top:40px;text-align:right}
  .person-name{font-size:22px;font-weight:700;color:var(--brown)}
  .person-title{font-size:14px;color:var(--ink)}
  .contact{position:absolute;left:300px;top:200px;list-style:none;font-size:14px;color:var(--ink)}
  .contact li{display:flex;align-items:center;gap:10px;height:22px}
  .contact .web{font-weight:700}
  .icon{width:15px;height:15px;flex:none}
  .card-back .brand{left:130px;top:104px}
  .card-back .brand-name{font-size:32px}
  .card-back .brand-tagline{position:absolute;left:158px;top:150px;font-size:12px}
  .rule{position:absolute;left:158px;top:176px;width:230px;height:1.5px;background:var(--brown)}
  .back-web{position:absolute;left:158px;top:186px;font-size:14px;color:var(--brown)}
</style>
</head>
<body>

<article class="card card-front">
  <svg class="decor" viewBox="0 0 560 320" aria-hidden="true">
    <path d="M300 0 C280 60 330 110 400 120 C470 130 500 200 560 210 L560 0 Z" fill="var(--blob)"/>
    <path d="M340 0 C330 40 380 80 440 90 C500 100 520 140 560 150 L560 0 Z" fill="var(--blob-soft)" opacity=".5"/>
  </svg>
  <div class="brand"><span class="brand-dot"></span><span class="brand-name">Brightwell Counseling</span></div>
  <p class="brand-tagline">a pro active addiction center</p>
  <div class="person">
    <p class="person-name">Maren Holt</p>
    <p class="person-title">Director</p>
  </div>
  <ul class="contact">
    <li><svg class="icon" viewBox="0 0 16 16"><circle cx="8" cy="8" r="7" fill="none" stroke="var(--brown)"/><path d="M5.5 4.5l1.5 1.5-1 1c.6 1.3 1.7 2.4 3 3l1-1 1.5 1.5-1 1.2c-2.8-.4-5.6-3.2-6-6z" fill="var(--brown)"/></svg>555.0142.318</li>
    <li><svg class="icon" viewBox="0 0 16 16"><circle cx="8" cy="8" r="7" fill="none" stroke="var(--brown)"/><rect x="4.5" y="6" width="7" height="5" fill="var(--brown)"/><rect x="5.5" y="4" width="5" height="2" fill="var(--brown)"/></svg>555.0167.905</li>
    <li><svg class="icon" viewBox="0 0 16 16"><circle cx="8" cy="8" r="7" fill="none" stroke="var(--brown)"/><rect x="4" y="5" width="8" height="6" fill="var(--brown)"/><path d="M4 5l4 3 4-3" stroke="var(--card-front)" fill="none"/></svg>m.holt@brightwell.com</li>
    <li class="web"><svg class="icon" viewBox="0 0 16 16"><circle cx="8" cy="8" r="7" fill="none" stroke="var(--brown)"/><circle cx="8" cy="8" r="4" fill="none" stroke="var(--brown)"/><path d="M4 8h8M8 4v8" stroke="var(--brown)"/></svg>www.brightwell.com</li>
  </ul>
</article>

<article class="card card-back">
  <svg class="decor" viewBox="0 0 560 320" aria-hidden="true">
    <path d="M70 60 C160 10 330 20 420 50 C500 80 520 170 470 240 C420 300 260 290 170 250 C80 210 20 110 70 60 Z" fill="var(--blob)"/>
    <path d="M440 0 C420 70 470 120 520 140 C545 150 560 170 560 190 L560 0 Z" fill="var(--blob-soft)" opacity=".6"/>
  </svg>
  <div class="brand"><span class="brand-dot"></span><span class="brand-name">Brightwell</span></div>
  <p class="brand-tagline">COUNSELING · a pro active addiction center</p>
  <span class="rule"></span>
  <p class="back-web">www.brightwell.com</p>
</article>

</body>
</html>
```